New Flyer Design Project

Needing brochure explaining the benefits of a home sleep study compared to a clinical hospital sleep study. We had our company logo designed by Vantro Works, we love it. We would like for it to be a bi-fold. See attachments for examples of information we would like to include.

```html
<!DOCTYPE html>
<html lang="en">
<head>
<meta charset="utf-8">
<title>Restwell Home Sleep Testing – Bi-fold Brochure</title>
<link rel="stylesheet" href="https://fonts.googleapis.com/css2?family=Montserrat:wght@400;500;600;700;800&family=Oswald:wght@600;700&display=swap">
<style>
:root{
  --navy:#1b4a86;
  --blue:#1f5ea8;
  --deep:#173f76;
  --green:#4cb848;
  --pale:#e9f2fa;
  --ink:#1f2a36;
  --line:#c9d8e8;
  --paper:#ffffff;
  --desk:#ececec;
}
*{margin:0;padding:0;box-sizing:border-box}
html,body{width:800px;height:1200px;overflow:hidden}
body{background:var(--desk);font-family:"Montserrat",sans-serif;color:var(--ink);position:relative}
.sheet{position:absolute;left:45px;width:710px;height:552px;background:var(--paper);overflow:hidden}
.sheet--outside{top:35px}
.sheet--inside{top:613px}
.abs{position:absolute}
.icon{width:1em;height:1em;fill:none;stroke:currentColor;stroke-width:2;stroke-linecap:round;stroke-linejoin:round;display:block}

/* brand */
.brand{position:absolute;display:flex;align-items:center;gap:8px}
.brand__dot{width:44px;height:44px;border-radius:50%;background:var(--blue);flex:none}
.brand__name{font-weight:800;color:var(--blue);font-size:25px;letter-spacing:-.5px;line-height:1}
.brand__tag{font-weight:700;color:var(--green);font-size:8px;letter-spacing:1px;margin-top:3px;text-align:center}
.brand--lg .brand__dot{width:62px;height:62px}
.brand--lg .brand__name{font-size:34px}
.brand--lg .brand__tag{font-size:10.5px}

.headline{position:absolute;font-family:"Oswald",sans-serif;font-weight:700;color:var(--navy);line-height:.95;font-size:28px;letter-spacing:.3px}
.headline .g{color:var(--green)}

.photo{position:absolute}

/* outside left */
.lede-title{left:25px;top:136px;font-weight:700;color:var(--blue);font-size:11.5px;line-height:1.05}
.lede{left:25px;top:167px;width:160px;font-size:9.4px;line-height:1.28;color:var(--ink)}

.compare{position:absolute;left:25px;top:257px;display:grid;grid-template-columns:97px 108px 108px;grid-auto-rows:29px}
.compare__head{height:25px;color:#fff;font-size:7px;font-weight:600;text-align:center;line-height:1.2;display:flex;align-items:center;justify-content:center;flex-direction:column}
.compare__head--home{background:var(--navy)}
.compare__head--lab{background:var(--green)}
.compare__label{display:flex;align-items:center;gap:5px;background:var(--pale);border:1.2px solid var(--navy);border-right:none;border-radius:15px 0 0 15px;margin:1px 0;font-size:7px;font-weight:700;color:var(--navy)}
.compare__label .disc{width:22px;height:22px;border-radius:50%;background:var(--navy);color:#fff;display:flex;align-items:center;justify-content:center;font-size:13px;margin-left:2px;flex:none}
.compare__cell{border:1.2px solid var(--navy);border-top:none;font-size:6.5px;line-height:1.2;display:flex;align-items:center;padding:0 6px 0 12px;background:#fff}
.compare__cell--home{color:var(--navy);position:relative}
.compare__cell--home .tick{position:absolute;left:4px;top:50%;margin-top:-6px;width:6px;height:6px;border-radius:50%;background:var(--green)}
.compare__cell--lab{border-left:none;color:#333}
.compare__head,.compare__cell{}

.band-navy{position:absolute;left:0;width:710px;background:var(--navy)}
.band-green{position:absolute;left:0;width:710px;background:var(--green)}
.site{position:absolute;color:#fff;font-size:8.5px;font-weight:600;display:flex;align-items:center;gap:4px}
.site .icon{font-size:8px;stroke-width:1.8}

.skip{left:25px;top:475px;display:flex;align-items:center;gap:10px;color:#fff;font-size:7.5px;font-weight:600;line-height:1.25}
.skip .ring{width:26px;height:26px;border-radius:50%;border:1.5px solid #fff;display:flex;align-items:center;justify-content:center;font-size:13px}
.result-box{left:203px;top:464px;width:136px;height:40px;background:#fff;border-radius:5px;border:1.5px solid var(--blue);display:flex;align-items:center;gap:8px;padding-left:9px}
.result-box .icon{font-size:22px;color:var(--green);stroke-width:1.6}
.result-box p{font-size:8px;font-weight:600;color:var(--blue);line-height:1.2}

/* outside right */
.tagline{left:375px;font-weight:700;color:var(--blue);font-size:9.6px}
.features{position:absolute;left:375px;top:190px;list-style:none}
.features li{display:flex;gap:11px;height:36px;align-items:flex-start}
.features .disc{width:25px;height:25px;border-radius:50%;border:1.5px solid var(--navy);color:var(--navy);display:flex;align-items:center;justify-content:center;font-size:14px;flex:none;margin-top:2px}
.features h3{font-size:10px;font-weight:700;color:var(--green);line-height:1.1}
.features p{font-size:7.4px;color:var(--navy);font-weight:500;line-height:1.25}

.perks{position:absolute;display:flex;justify-content:space-between;text-align:center}
.perk{color:#fff;font-size:6.6px;font-weight:600;letter-spacing:.3px;line-height:1.2}
.perk .ring{width:42px;height:42px;border-radius:50%;border:2px solid #fff;margin:0 auto 7px;display:flex;align-items:center;justify-content:center;font-size:24px}
.perk .ring .icon{stroke-width:2.2}

/* inside left */
.cpap-title{left:25px;font-weight:800;color:var(--blue);line-height:1}
.cpap-body{left:25px;top:139px;width:150px;font-size:6.6px;line-height:1.63;color:#2a2a2a}
.cpap-body p{margin-bottom:6px}

.problem{left:180px;top:152px;width:155px;height:81px;border:1.3px solid var(--blue);border-radius:6px;padding:10px 12px 0 16px;background:#fff}
.problem h3{font-size:9.5px;font-weight:800;color:var(--blue);line-height:1}
.problem .sub{font-size:6.8px;font-weight:700;color:var(--green);line-height:1.2;margin-top:2px;width:95px}
.problem .txt{font-size:6.8px;color:#222;line-height:1.2;margin-top:3px}
.problem .warn{position:absolute;right:10px;top:8px;font-size:30px;color:#f29a1b;stroke-width:1.6}

.lab-list{left:180px;top:243px;width:155px;height:144px;background:var(--blue);border-radius:6px;padding:8px 8px 0 8px;color:#fff}
.lab-list h3{font-size:7.4px;font-weight:700;margin-bottom:5px}
.lab-list ul{list-style:none}
.lab-list li{display:flex;gap:5px;font-size:6.4px;line-height:1.05;margin-bottom:6px}
.lab-list li .x{width:10px;height:10px;border-radius:50%;background:#fff;color:var(--green);flex:none;font-size:10px;display:flex;align-items:center;justify-content:center}
.lab-list li .x .icon{stroke-width:3;font-size:8px}

.device-label{left:260px;top:397px;font-size:6.2px;color:#222;font-weight:500}
.ok-badge{left:317px;top:402px;width:28px;height:28px;border-radius:50%;background:var(--green);border:2px solid #fff;color:#fff;display:flex;align-items:center;justify-content:center;font-size:17px}
.ok-badge .icon{stroke-width:3}

/* inside right */
.smart{left:355px;width:355px;text-align:center;font-family:"Oswald",sans-serif;font-weight:700;font-size:27px;line-height:1;color:var(--navy)}
.smart-sub{left:355px;width:355px;text-align:center;top:79px;font-size:9.6px;font-weight:700;color:var(--blue);line-height:1.35}

.choice{position:absolute;left:376px;top:111px;width:309px;border:1px solid var(--line);border-radius:8px;overflow:hidden;display:grid;grid-template-columns:86px 108px 115px;grid-template-rows:33px repeat(7,32.2px)}
.choice__h{color:#fff;font-weight:700;display:flex;flex-direction:column;align-items:center;justify-content:center;font-size:9px;line-height:1.05}
.choice__h small{font-size:6.5px;font-weight:600;margin-top:1px}
.choice__h--f{background:var(--navy);font-size:9.5px}
.choice__h--home{background:var(--green)}
.choice__h--lab{background:var(--navy)}
.choice__c{display:flex;align-items:center;gap:5px;border-top:1px solid var(--line);font-size:6.7px;line-height:1.1;padding:0 5px}
.choice__c + .choice__c{border-left:1px solid var(--line)}
.choice__c--f{font-weight:700;color:var(--navy);padding-left:10px;gap:7px}
.choice__c--f .icon{font-size:15px;flex:none;stroke-width:2.2}
.choice__c--home{color:var(--navy);padding-left:10px}
.choice__c--lab{color:#444;padding-left:10px}
.mark{width:10px;height:10px;border-radius:50%;flex:none;display:flex;align-items:center;justify-content:center;color:#fff;font-size:8px}
.mark .icon{stroke-width:3.4}
.mark--yes{background:var(--green)}
.mark--no{background:#6c7480}

.cta{left:410px;top:380px;display:flex;align-items:center;gap:5px}
.cta .ring{width:31px;height:31px;border-radius:50%;border:1.6px solid var(--navy);color:var(--navy);display:flex;align-items:center;justify-content:center;font-size:17px}
.cta h3{font-family:"Oswald",sans-serif;font-weight:700;color:var(--navy);font-size:16px;line-height:1;letter-spacing:.3px}
.cta p{font-size:8px;font-weight:600;color:var(--blue);margin-top:2px}
.phone{left:410px;top:419px;width:239px;height:26px;border-radius:13px;background:var(--green);color:#fff;display:flex;align-items:center;justify-content:center;gap:8px;font-weight:700;font-size:16px;letter-spacing:.5px}
.phone .ring{width:20px;height:20px;border-radius:50%;border:1.5px solid #fff;display:flex;align-items:center;justify-content:center;font-size:11px}

.strip{position:absolute;left:20px;top:470px;width:670px;display:flex;justify-content:space-between;text-align:center}
.strip .perk{width:84px;font-size:6.4px}
.strip .perk .icon{font-size:17px;margin:0 auto 6px;stroke-width:2.2}
</style>
</head>
<body>

<svg width="0" height="0" style="position:absolute" aria-hidden="true">
  <defs>
    <symbol id="i-home" viewBox="0 0 24 24"><path d="M3 11.5 12 3.5l9 8M6 9.5V20h12V9.5M10 20v-5h4v5"/></symbol>
    <symbol id="i-clock" viewBox="0 0 24 24"><circle cx="12" cy="12" r="9"/><path d="M8 10.5l4 3.5 4-4"/></symbol>
    <symbol id="i-dollar" viewBox="0 0 24 24"><path d="M15.5 7.5c-.8-1.1-2.1-1.7-3.5-1.7-2 0-3.6 1-3.6 2.7 0 3.8 7.2 2 7.2 5.8 0 1.7-1.6 2.9-3.6 2.9-1.5 0-2.9-.6-3.8-1.7M12 3.5v17"/></symbol>
    <symbol id="i-bed" viewBox="0 0 24 24"><path d="M3 6v14M3 16h18v4M21 16v-3a2 2 0 0 0-2-2h-8v5"/><circle cx="7" cy="13" r="1.6"/><path d="M15 4h3l-3 3h3"/></symbol>
    <symbol id="i-hand" viewBox="0 0 24 24"><path d="M3 14h4l4 2h5a1.5 1.5 0 0 1 0 3h-5M7 20l4 1 9-3.5"/><path d="M10 7.5l2 2 4-4"/></symbol>
    <symbol id="i-shield" viewBox="0 0 24 24"><path d="M12 3l7 3v5c0 5-3 8-7 10-4-2-7-5-7-10V6z"/><path d="M9 12l2 2 4-4"/></symbol>
    <symbol id="i-flask" viewBox="0 0 24 24"><path d="M9 3h6M10 3v6l-5 10a1.4 1.4 0 0 0 1.3 2h11.4a1.4 1.4 0 0 0 1.3-2L14 9V3M7.5 15h9"/></symbol>
    <symbol id="i-clip" viewBox="0 0 24 24"><path d="M8 4H6v17h9M16 4h2v9"/><rect x="8" y="3" width="8" height="3" rx="1"/><path d="M9 10h6M9 13h6M9 16h3"/><circle cx="18" cy="18" r="3.5"/><path d="M16.5 18l1 1 2-2"/></symbol>
    <symbol id="i-badge" viewBox="0 0 24 24"><circle cx="12" cy="12" r="9"/><path d="M8 12.5l3 3 5-6"/></symbol>
    <symbol id="i-person" viewBox="0 0 24 24"><circle cx="10" cy="8" r="3.5"/><path d="M3.5 20c0-4 3-6.5 6.5-6.5 1.3 0 2.4.3 3.4.8"/><circle cx="17.5" cy="17.5" r="3.5"/><path d="M16 17.5l1 1 2-2"/></symbol>
    <symbol id="i-cal" viewBox="0 0 24 24"><rect x="4" y="5" width="16" height="15" rx="1.5"/><path d="M4 9h16M8 3v4M16 3v4M9 14l2 2 4-4"/></symbol>
    <symbol id="i-moon" viewBox="0 0 24 24"><path d="M19 15A8 8 0 1 1 9 5a6.5 6.5 0 0 0 10 10z"/><path d="M15 4h3l-3 3h3"/></symbol>
    <symbol id="i-check" viewBox="0 0 24 24"><path d="M5 12.5l4.5 4.5L19 7.5"/></symbol>
    <symbol id="i-x" viewBox="0 0 24 24"><path d="M7 7l10 10M17 7 7 17"/></symbol>
    <symbol id="i-wave" viewBox="0 0 24 24"><circle cx="12" cy="12" r="9"/><path d="M3.5 12h4l2-4 3 8 2-4h6"/></symbol>
    <symbol id="i-doc" viewBox="0 0 24 24"><rect x="5" y="3" width="14" height="18" rx="2"/><path d="M9 8h6M9 12h6M9 16h4"/></symbol>
    <symbol id="i-gear" viewBox="0 0 24 24"><circle cx="12" cy="12" r="3"/><path d="M12 2.5v3M12 18.5v3M2.5 12h3M18.5 12h3M5.3 5.3l2.1 2.1M16.6 16.6l2.1 2.1M5.3 18.7l2.1-2.1M16.6 7.4l2.1-2.1"/><circle cx="12" cy="12" r="6.5"/></symbol>
    <symbol id="i-cart" viewBox="0 0 24 24"><path d="M3 5h3l2.5 10h10L21 8H7.2"/><circle cx="10" cy="19" r="1.3"/><circle cx="17" cy="19" r="1.3"/><path d="M10 11h8"/></symbol>
    <symbol id="i-phone" viewBox="0 0 24 24"><path d="M5 4h4l2 5-2.5 1.5a11 11 0 0 0 5 5L15 13l5 2v4a1 1 0 0 1-1 1A16 16 0 0 1 4 5a1 1 0 0 1 1-1z"/></symbol>
    <symbol id="i-warn" viewBox="0 0 24 24"><path d="M12 3 2 20.5h20z"/><path d="M12 9.5v5.5M12 17.5v.3"/></symbol>
    <symbol id="i-globe" viewBox="0 0 24 24"><circle cx="12" cy="12" r="9"/><path d="M3 12h18M12 3c3 3 3 15 0 18M12 3c-3 3-3 15 0 18"/></symbol>
  </defs>
</svg>

<!-- ================= OUTSIDE SPREAD ================= -->
<section class="sheet sheet--outside">

  <!-- left panel -->
  <div class="photo" role="img" aria-label="Photo of a wrist-worn home sleep test device with finger probe and chest sensor on a light wooden table"
       style="left:160px;top:0;width:195px;height:240px;background:radial-gradient(ellipse at 60% 45%,#f7f7f5 0%,#e7e2da 55%,#d6cfc4 100%)"></div>
  <svg class="abs" style="left:0;top:150px" width="355" height="110" viewBox="0 0 355 110" aria-hidden="true">
    <path d="M0 75 C110 95 240 70 355 15 V110 H0Z" fill="#fff"/>
    <path d="M0 78 C120 92 250 70 355 18 V30 C240 95 110 112 0 98Z" fill="#1b4a86"/>
    <path d="M150 95 C240 85 300 55 355 30 V44 C300 70 230 95 150 95Z" fill="#4cb848"/>
    <path d="M0 98 C110 112 240 95 355 30 V110 H0Z" fill="#fff"/>
  </svg>

  <div class="brand" style="left:25px;top:27px">
    <span class="brand__dot"></span>
    <div><div class="brand__name">RESTWELL</div><div class="brand__tag">• HOME SLEEP TESTING •</div></div>
  </div>

  <h1 class="headline" style="left:25px;top:84px">BETTER <span class="g">SLEEP</span><br>STARTS AT HOME</h1>
  <h2 class="abs lede-title">Home Sleep Study vs.<br>Clinical Sleep Study</h2>
  <p class="abs lede">Get answers faster, spend less and sleep better—right from the comfort of your own home.</p>

  <div class="compare">
    <div></div>
    <div class="compare__head compare__head--home"><span>HOME SLEEP STUDY</span><span>with RESTWELL</span></div>
    <div class="compare__head compare__head--lab"><span>CLINICAL SLEEP STUDY</span><span>in a sleep lab</span></div>

    <div class="compare__label"><span class="disc"><svg class="icon"><use href="#i-home"/></svg></span>COMFORT</div>
    <div class="compare__cell compare__cell--home"><span class="tick"></span>Sleep in your own bed in a familiar environment</div>
    <div class="compare__cell compare__cell--lab">Unfamiliar environment, harder to relax</div>

    <div class="compare__label"><span class="disc"><svg class="icon"><use href="#i-clock"/></svg></span>TIME TO RESULTS</div>
    <div class="compare__cell compare__cell--home"><span class="tick"></span>Results in less than 72 hours</div>
    <div class="compare__cell compare__cell--lab">Results can take weeks, or even months</div>

    <div class="compare__label"><span class="disc"><svg class="icon"><use href="#i-dollar"/></svg></span>COST</div>
    <div class="compare__cell compare__cell--home"><span class="tick"></span>Affordable — just $289</div>
    <div class="compare__cell compare__cell--lab">Expensive — often $1,000 – $5,000</div>

    <div class="compare__label"><span class="disc"><svg class="icon"><use href="#i-bed"/></svg></span>SLEEP QUALITY</div>
    <div class="compare__cell compare__cell--home"><span class="tick"></span>More natural sleep in your own environmet</div>
    <div class="compare__cell compare__cell--lab">Harder to sleep with wires, unfamiliar setting</div>

    <div class="compare__label"><span class="disc"><svg class="icon"><use href="#i-hand"/></svg></span>CONVENIENCE</div>
    <div class="compare__cell compare__cell--home"><span class="tick"></span>Easy, simple test you do at home</div>
    <div class="compare__cell compare__cell--lab">Requires overnight stay at a sleep center</div>

    <div class="compare__label"><span class="disc"><svg class="icon"><use href="#i-shield"/></svg></span>ACCURACY</div>
    <div class="compare__cell compare__cell--home"><span class="tick"></span>Board certified sleep physicians ensure accurate results</div>
    <div class="compare__cell compare__cell--lab">Accurate results, but often unnecessary for many patients</div>
  </div>

  <!-- right panel -->
  <div class="photo" role="img" aria-label="Photo of a hand wearing a home sleep test wrist device with finger sensor, on a soft white bed"
       style="left:541px;top:92px;width:169px;height:300px;background:radial-gradient(ellipse at 45% 50%,#e9c3a6 0%,#f1e4da 45%,#f4f4f4 100%)"></div>
  <svg class="abs" style="left:355px;top:295px" width="355" height="170" viewBox="0 0 355 170" aria-hidden="true">
    <path d="M0 37 C90 45 120 95 200 95 C270 95 320 50 355 5 V170 H0Z" fill="#1b4a86"/>
    <path d="M130 78 C200 110 290 80 355 5 V22 C300 85 220 108 150 88Z" fill="#4cb848"/>
  </svg>

  <div class="band-navy" style="top:457px;height:60px"></div>
  <div class="band-green" style="top:517px;height:35px"></div>

  <div class="brand brand--lg" style="left:373px;top:21px">
    <span class="brand__dot"></span>
    <div><div class="brand__name">RESTWELL</div><div class="brand__tag">• HOME SLEEP TESTING •</div></div>
  </div>
  <h2 class="headline" style="left:375px;top:101px">BETTER <span class="g">SLEEP</span><br>STARTS AT HOME</h2>
  <p class="abs tagline" style="top:153px">Accurate. Affordable. Convenient.</p>
  <p class="abs tagline" style="top:169px">Home Sleep Testing Made Simple.</p>

  <ul class="features">
    <li><span class="disc"><svg class="icon"><use href="#i-home"/></svg></span><div><h3>TEST AT HOME</h3><p>Sleep in your own bed,<br>in your own environment.</p></div></li>
    <li><span class="disc"><svg class="icon"><use href="#i-badge"/></svg></span><div><h3>FDA APPROVED</h3><p>A-Fib flagging system flags<br>potential A-Fib events.</p></div></li>
    <li><span class="disc"><svg class="icon"><use href="#i-doc"/></svg></span><div><h3>FAST RESULTS</h3><p>Get clear, board-certified<br>results in lass than 72 hours.</p></div></li>
    <li><span class="disc"><svg class="icon"><use href="#i-dollar"/></svg></span><div><h3>AFFORDABLE</h3><p>No surprise bills. No insurance<br>hoops. Just one low price.</p></div></li>
  </ul>

  <div class="perks" style="left:370px;top:429px;width:330px">
    <div class="perk" style="width:78px"><div class="ring"><svg class="icon"><use href="#i-home"/></svg></div>SLEEP IN YOUR<br>OWN BED</div>
    <div class="perk" style="width:78px"><div class="ring"><svg class="icon"><use href="#i-clock"/></svg></div>RESULTS IN LESS<br>THAN 72 HOURS</div>
    <div class="perk" style="width:78px"><div class="ring"><svg class="icon"><use href="#i-dollar"/></svg></div>AFFORDABLE –<br>JUST $289</div>
    <div class="perk" style="width:78px"><div class="ring"><svg class="icon"><use href="#i-person"/></svg></div>BOARD CERTIFIED<br>SLEEP PHTSICIANS</div>
  </div>

  <div class="abs skip"><span class="ring"><svg class="icon"><use href="#i-flask"/></svg></span><p>SKIP THE LABS. SKIP THE STRESS.<br>JUST A SIMPLE TEST AT HOME.</p></div>
  <div class="abs result-box"><svg class="icon"><use href="#i-clip"/></svg><p>SLEEP APNEA TEST<br>RESULTS IN LESS<br>THAN 72 HOURS</p></div>
  <p class="site" style="left:131px;top:525px"><svg class="icon"><use href="#i-globe"/></svg>www.restwellhome.example</p>
</section>

<!-- ================= INSIDE SPREAD ================= -->
<section class="sheet sheet--inside">

  <!-- left panel -->
  <div class="photo" role="img" aria-label="Photo of a man sleeping on a white pillow wearing a CPAP nasal mask"
       style="left:189px;top:0;width:166px;height:170px;background:linear-gradient(200deg,#d9c3a8 0%,#ece6de 45%,#fff 100%)"></div>

  <div class="brand" style="left:25px;top:22px">
    <span class="brand__dot"></span>
    <div><div class="brand__name">RESTWELL</div><div class="brand__tag">• HOME SLEEP TESTING •</div></div>
  </div>
  <h2 class="abs cpap-title" style="top:78px;font-size:14.5px">CPAP THERAPY</h2>
  <h3 class="abs cpap-title" style="top:97px;font-size:17px;color:var(--green)">WHAT IS CPAP?</h3>
  <h4 class="abs cpap-title" style="top:116px;font-size:12px;font-weight:600">CPAP &amp; MASKS</h4>

  <div class="abs cpap-body">
    <p>CPAP (pronounced "see-pap") stands for Continuous Positive Airway Pressure, and is currently the most popular and effective way to treat sleep apnea.</p>
    <p>The airway collapse that is associated with sleep apnea occurs following exhalation when the patient begins to draw the next breath. This creates a vacuum in the airway as the diaphragm muscle tries to pull the air into the lungs. CPAP prevents this vacuum by providing pressurized air to pneumatically splint the airway open. For people suffering from sleep apnea, CPAP provides immediate relief.</p>
    <p>Although the idea behind CPAP is simple, the application requires study and expertise. CPAP devices must be prescribed by a physician. A CPAP range is prescribed for each patient. We only use degreed clinicians for prescribed therapy. Alway ask for what type of credentials your provider has.</p>
  </div>

  <div class="abs problem">
    <h3>THE PROBLEM</h3>
    <p class="sub">Sleep care wasn't built with people in mind.</p>
    <p class="txt">Most people wait months, spend a fortune, and end up feeling more like a chart than a human. It doesn't have to be this way.</p>
    <svg class="icon warn"><use href="#i-warn"/></svg>
  </div>

  <div class="abs lab-list">
    <h3>TRADITIONAL SLEEP LAB WORKS:</h3>
    <ul>
      <li><span class="x"><svg class="icon"><use href="#i-x"/></svg></span>Waiting 2-3 months just to be seen, all while you're tired, foggy, and trying to keep life together.</li>
      <li><span class="x"><svg class="icon"><use href="#i-x"/></svg></span>Sleeping in a medical facility with 20+ wires taped everywhere.</li>
      <li><span class="x"><svg class="icon"><use href="#i-x"/></svg></span>Surprise bills ranging from $1,000-$5,000.</li>
      <li><span class="x"><svg class="icon"><use href="#i-x"/></svg></span>Delays of weeks or months for results that should be quick.</li>
      <li><span class="x"><svg class="icon"><use href="#i-x"/></svg></span>Getting pushed into buying equipment at inflated prices because there are no alternatives.</li>
    </ul>
  </div>

  <div class="photo" role="img" aria-label="Product photos of four CPAP masks and a CPAP machine"
       style="left:20px;top:393px;width:335px;height:62px;background:linear-gradient(180deg,#fff 0%,#eef1f3 60%,#dfeede 100%)"></div>
  <p class="abs device-label">AIRFLOW CPAP</p>
  <div class="abs ok-badge"><svg class="icon"><use href="#i-check"/></svg></div>

  <!-- right panel -->
  <h2 class="abs smart" style="top:19px">HOME SLEEP TESTING</h2>
  <h2 class="abs smart" style="top:45px;color:var(--green)">THE SMARTER CHOICE</h2>
  <p class="abs smart-sub">Why more people are choosing home sleep testing<br>over traditional sleep labs.</p>

  <div class="choice">
    <div class="choice__h choice__h--f">FEATURE</div>
    <div class="choice__h choice__h--home">HOME SLEEP STUDY<small>( NIGHTTRACE ONE )</small></div>
    <div class="choice__h choice__h--lab">CLINICAL SLEEP STUDY<small>( IN-HOSPITAL )</small></div>

    <div class="choice__c choice__c--f"><svg class="icon"><use href="#i-bed"/></svg>Comfort</div>
    <div class="choice__c choice__c--home"><span class="mark mark--yes"><svg class="icon"><use href="#i-check"/></svg></span>Sleep in your own bed</div>
    <div class="choice__c choice__c--lab"><span class="mark mark--no"><svg class="icon"><use href="#i-x"/></svg></span>Unfamiliar environment</div>

    <div class="choice__c choice__c--f"><svg class="icon"><use href="#i-home"/></svg>Convenience</div>
    <div class="choice__c choice__c--home"><span class="mark mark--yes"><svg class="icon"><use href="#i-check"/></svg></span>No travel or<br>overnight stay</div>
    <div class="choice__c choice__c--lab"><span class="mark mark--no"><svg class="icon"><use href="#i-x"/></svg></span>Travel and<br>overnight stay</div>

    <div class="choice__c choice__c--f"><svg class="icon"><use href="#i-clock"/></svg>Wait Time</div>
    <div class="choice__c choice__c--home"><span class="mark mark--yes"><svg class="icon"><use href="#i-check"/></svg></span>Test in a day or two</div>
    <div class="choice__c choice__c--lab"><span class="mark mark--no"><svg class="icon"><use href="#i-x"/></svg></span>Wait weeks or months</div>

    <div class="choice__c choice__c--f"><svg class="icon"><use href="#i-dollar"/></svg>Cost</div>
    <div class="choice__c choice__c--home"><span class="mark mark--yes"><svg class="icon"><use href="#i-check"/></svg></span>$289 flat rate</div>
    <div class="choice__c choice__c--lab"><span class="mark mark--no"><svg class="icon"><use href="#i-x"/></svg></span>$1,000 – $5,000<br>or more</div>

    <div class="choice__c choice__c--f"><svg class="icon"><use href="#i-wave"/></svg>Wires &amp;<br>Sensors</div>
    <div class="choice__c choice__c--home"><span class="mark mark--yes"><svg class="icon"><use href="#i-check"/></svg></span>Simple, comfortable<br>wrist device</div>
    <div class="choice__c choice__c--lab"><span class="mark mark--no"><svg class="icon"><use href="#i-x"/></svg></span>20+ wires taped<br>everywhere</div>

    <div class="choice__c choice__c--f"><svg class="icon"><use href="#i-doc"/></svg>Results</div>
    <div class="choice__c choice__c--home"><span class="mark mark--yes"><svg class="icon"><use href="#i-check"/></svg></span>Results in less<br>than 72 hours</div>
    <div class="choice__c choice__c--lab"><span class="mark mark--no"><svg class="icon"><use href="#i-x"/></svg></span>Delays of weeks<br>or months</div>

    <div class="choice__c choice__c--f" style="padding-left:6px;gap:5px"><svg class="icon"><use href="#i-gear"/></svg>Post Diagnosis<br>of O.S.A.</div>
    <div class="choice__c choice__c--home" style="font-size:6.3px"><span class="mark mark--yes"><svg class="icon"><use href="#i-check"/></svg></span>We only use Respiratory Therapist, Nurses or Sleep Techs for clinical services</div>
    <div class="choice__c choice__c--lab"><span class="mark mark--no"><svg class="icon"><use href="#i-x"/></svg></span>May use anybody without a degree in healthcare</div>
  </div>

  <div class="abs cta">
    <span class="ring"><svg class="icon"><use href="#i-cart"/></svg></span>
    <div><h3>TAKE CONTROL OF YOUR SLEEP</h3><p>Order your NightTrace One Home Sleep Test today.</p></div>
  </div>
  <div class="abs phone"><span class="ring"><svg class="icon"><use href="#i-phone"/></svg></span>555-014-2290</div>

  <div class="band-navy" style="top:455px;height:63px"></div>
  <div class="band-green" style="top:518px;height:34px"></div>

  <div class="strip">
    <div class="perk"><svg class="icon"><use href="#i-home"/></svg>SLEEP IN YOUR<br>OWN BED</div>
    <div class="perk"><svg class="icon"><use href="#i-clock"/></svg>RESULTS IN LESS<br>THAN 72 HOURS</div>
    <div class="perk"><svg class="icon"><use href="#i-dollar"/></svg>AFFORDABLE –<br>JUST $289</div>
    <div class="perk"><svg class="icon"><use href="#i-person"/></svg>BOARD CERTIFIED<br>SLEEP PHTSICIANS</div>
    <div class="perk"><svg class="icon"><use href="#i-badge"/></svg>FDA APPROVED</div>
    <div class="perk"><svg class="icon"><use href="#i-cal"/></svg>NO APPOINTMENTS<br>NO INSURANCE CHAOS</div>
    <div class="perk"><svg class="icon"><use href="#i-bed"/></svg>ONE COMFORTABLE<br>NIGHT - REAL RESULTS</div>
    <div class="perk"><svg class="icon"><use href="#i-moon"/></svg>BETTER SLEEP<br>BETTER YOU</div>
  </div>

  <p class="site" style="left:480px;top:525px"><svg class="icon"><use href="#i-globe"/></svg>www.restwellhome.example</p>
</section>

</body>
</html>
```